coral ridge bathrooms

We are in the business of renovating peoples bathrooms and tiling service

we provide a total solution from design to reconstruction of your bathroom

we would like a 5 page website

please design the home page first so we choose design then complete the other 4 pages i have uploaded the logo

Industry/Entity Type

Business

```html
<!DOCTYPE html>
<html lang="en">
<head>
<meta charset="utf-8">
<title>Coral Ridge Bathrooms – Services</title>
<link rel="stylesheet" href="https://fonts.googleapis.com/css2?family=PT+Sans+Narrow:wght@400;700&family=PT+Sans:wght@400;700&display=swap">
<style>
  :root {
    --header-bg: #2b2627;
    --footer-bg: #2d2829;
    --gold: #b89a2c;
    --gold-card: #967a17;
    --gold-accent: #c29c2f;
    --text-light: #ffffff;
    --text-muted: #dcd3c3;
    --divider: #151213;
    --photo-left-a: #6b6a52;
    --photo-left-b: #3a2f2a;
    --photo-right-a: #9c9a8c;
    --photo-right-b: #5f5c52;
  }
  * { margin: 0; padding: 0; box-sizing: border-box; }
  html, body { width: 1200px; height: 709px; overflow: hidden; }
  body {
    position: relative;
    font-family: "PT Sans", sans-serif;
    background: var(--header-bg);
    color: var(--text-light);
  }

  /* Header */
  .site-header { position: absolute; left: 0; top: 0; width: 1200px; height: 126px; background: var(--header-bg); }
  .brand {
    position: absolute; left: 160px; top: 44px;
    display: flex; align-items: center; gap: 10px;
    font-family: "PT Sans Narrow", sans-serif; font-weight: 700;
    font-size: 22px; letter-spacing: 0.5px; color: var(--gold-accent);
    text-transform: uppercase;
  }
  .brand-mark { width: 22px; height: 22px; background: var(--gold-accent); }
  .social { position: absolute; right: 158px; top: 17px; display: flex; gap: 8px; }
  .social-tile { width: 22px; height: 22px; border-radius: 3px; background: #8c8887; }
  .call-now {
    position: absolute; right: 158px; top: 43px;
    font-family: "PT Sans Narrow", sans-serif; font-weight: 700; font-size: 13.5px;
    color: var(--text-light);
  }
  .main-nav { position: absolute; right: 158px; top: 78px; display: flex; align-items: center; }
  .main-nav a {
    font-family: "PT Sans Narrow", sans-serif; font-weight: 700; font-size: 14px;
    color: var(--text-light); text-decoration: none; padding: 0 15px;
    border-left: 1px solid var(--divider); line-height: 20px;
  }
  .main-nav a:first-child { border-left: none; }
  .main-nav a:last-child { padding-right: 0; }
  .main-nav a.is-active { color: var(--gold-accent); }

  /* Stage */
  .stage { position: absolute; left: 0; top: 126px; width: 1200px; height: 514px; }
  .backdrop-left, .backdrop-right { position: absolute; top: 0; height: 514px; }
  .backdrop-left { left: 0; width: 157px; background: linear-gradient(180deg, var(--photo-left-a), #8a8060 55%, var(--photo-left-b)); }
  .backdrop-right { right: 0; width: 157px; background: linear-gradient(180deg, var(--photo-right-a), #b0ab9c 50%, var(--photo-right-b)); }
  .content-panel { position: absolute; left: 157px; top: 0; width: 886px; height: 514px; background: var(--gold); }
  .section-title {
    position: absolute; left: 19px; top: 36px;
    font-family: "PT Sans Narrow", sans-serif; font-weight: 700; font-size: 19px;
    color: var(--text-light); text-transform: uppercase;
  }
  .service-card { position: absolute; left: 19px; width: 848px; height: 191px; background: var(--gold-card); }
  .service-card--bathroom { top: 84px; }
  .service-card--tiling { top: 296px; }
  .service-arrow { position: absolute; left: 20px; top: 21px; }
  .service-title {
    position: absolute; left: 41px; top: 22px;
    font-family: "PT Sans Narrow", sans-serif; font-weight: 700; font-size: 14px;
    text-transform: uppercase; color: var(--text-light);
  }
  .service-text {
    position: absolute; left: 42px; top: 52px; width: 452px; height: 89px; overflow: hidden;
    font-size: 11.4px; line-height: 17.6px; text-align: justify; color: var(--text-light);
  }
  .service-photo {
    position: absolute; left: 512px; top: 18px; width: 323px; height: 155px;
    border: 2px solid #ffffff; border-radius: 4px;
  }
  .service-photo--bathroom { background: linear-gradient(135deg, #d9b98a, #f2e6cc 45%, #b98a55); }
  .service-photo--tiling { background: linear-gradient(135deg, #e9e9e9, #f5f5f5 45%, #8a2a2a 75%, #262626); }

  /* Footer */
  .site-footer { position: absolute; left: 0; top: 640px; width: 1200px; height: 69px; background: var(--footer-bg); }
  .copyright { position: absolute; left: 159px; top: 26px; font-size: 12px; color: var(--text-muted); }
  .footer-nav { position: absolute; right: 158px; top: 26px; display: flex; font-size: 12px; color: var(--text-muted); }
  .footer-nav a { color: var(--text-muted); text-decoration: none; }
  .footer-nav .sep { padding: 0 16px; }
</style>
</head>
<body>
  <header class="site-header">
    <div class="brand"><span class="brand-mark"></span>Coral Ridge Bathrooms</div>
    <div class="social" aria-label="Social links">
      <span class="social-tile"></span><span class="social-tile"></span><span class="social-tile"></span>
    </div>
    <div class="call-now">CALL NOW : 4410-562-07</div>
    <nav class="main-nav">
      <a href="#">HOME</a><a href="#">ABOUT US</a><a href="#">SERVICES</a><a href="#" class="is-active">GALLERY</a><a href="#">CONTACT US</a>
    </nav>
  </header>

  <main class="stage">
    <div class="backdrop-left" role="img" aria-label="Bathroom vanity with plants and dark wooden drawers"></div>
    <div class="backdrop-right" role="img" aria-label="Tiled shower with glass door and spa accessories"></div>
    <section class="content-panel">
      <h1 class="section-title">Our General Services</h1>

      <article class="service-card service-card--bathroom">
        <svg class="service-arrow" width="10" height="20" viewBox="0 0 10 20"><polygon points="1,0 9,10 1,20" fill="#111"/></svg>
        <h2 class="service-title">Bathroom Reconstructions</h2>
        <p class="service-text">It has roots in a piece of it over 2000 years old. Contrary to popular belief, Lorem Ipsum is not simply random text. It has roots in a piece of classical Latin literature from 45 BC, making it over 2000 years old. Martin Hollis, a Latin professor at Westbrook College in Vermont, looked up one of the more obscure Latin words, consectetur, from a Lorem Ipsum passage, and going through the cites of the word in</p>
        <div class="service-photo service-photo--bathroom" role="img" aria-label="Renovated bathroom with corner bathtub and wall basin"></div>
      </article>

      <article class="service-card service-card--tiling">
        <svg class="service-arrow" width="10" height="20" viewBox="0 0 10 20"><polygon points="1,0 9,10 1,20" fill="#111"/></svg>
        <h2 class="service-title">Tiling Services</h2>
        <p class="service-text">It has roots in a piece of it over 2000 years old. Contrary to popular belief, Lorem Ipsum is not simply random text. It has roots in a piece of classical Latin literature from 45 BC, making it over 2000 years old. Martin Hollis, a Latin professor at Westbrook College in Vermont, looked up one of the more obscure Latin words, consectetur, from a Lorem Ipsum passage, and going through the cites of the word in</p>
        <div class="service-photo service-photo--tiling" role="img" aria-label="Modern tiled kitchen with red chairs and mosaic wall"></div>
      </article>
    </section>
  </main>

  <footer class="site-footer">
    <p class="copyright">© 2013 All Right Reserved By Coral Ridge Bathrooms</p>
    <nav class="footer-nav">
      <a href="#">Home</a><span class="sep">|</span><a href="#">About</a><span class="sep">|</span><a href="#">Service</a><span class="sep">|</span><a href="#">Gallery</a><span class="sep">|</span><a href="#">Contact Us</a>
    </nav>
  </footer>
</body>
</html>
```